Business card

We are looking for a creative person to deigns our company business card.

Target Market(s)

College age student

Industry/Entity Type

Accommodation

Contact Information for Business Card

We want a fun, clean and sophisticated design. It should look good, but more importantly the information should be legible.

Font styles to use
Serif
Sans Serif
Other font styles liked:
• Open Sans ,

Colors
33a6d7

Requirements
Must have
• Must have a young and memorable message. Be legible.
• Our logo on the back on a solid blue , please find color and logo attached
• LodgeBridgely.net on the back.
Nice to have
• I would like to have couple of different fonts on the LodgeBridgely.net on the back of the cards with a solid blue.

```html
<!DOCTYPE html>
<html lang="en">
<head>
<meta charset="utf-8">
<title>LodgeBridgely Business Card</title>
<link href="https://fonts.googleapis.com/css2?family=Signika:wght@400;600&display=swap" rel="stylesheet">
<style>
  :root {
    --page-bg: #e9e7e3;
    --card-light: #eef0f1;
    --card-light-edge: #dfe3e5;
    --panel-blue-top: #2a6a95;
    --panel-blue-bottom: #1b4f78;
    --edge-teal: #3a8aa3;
    --panel-text: #e4ebef;
    --panel-text-soft: #cfdbe2;
    --brand-text: #1d5a80;
  }
  html, body {
    margin: 0;
    padding: 0;
    width: 1200px;
    height: 1054px;
    overflow: hidden;
    background: var(--page-bg);
    font-family: "Signika", "Open Sans", sans-serif;
  }
  .business-card {
    position: absolute;
    left: 100px;
    top: 225px;
    width: 1000px;
    height: 603px;
    background: linear-gradient(160deg, var(--card-light), var(--card-light-edge));
    border-radius: 4px;
    overflow: hidden;
    box-shadow: 0 10px 30px rgba(0,0,0,0.18);
  }
  .card-shapes {
    position: absolute;
    inset: 0;
  }
  .contact-panel {
    position: absolute;
    left: 53px;
    top: 0;
    color: var(--panel-text);
  }
  .person-name {
    position: absolute;
    top: 70px;
    left: 0;
    margin: 0;
    font-size: 39px;
    font-weight: 600;
    white-space: nowrap;
  }
  .person-role {
    position: absolute;
    top: 127px;
    left: 0;
    margin: 0;
    font-size: 23px;
    font-weight: 400;
    white-space: nowrap;
    color: var(--panel-text-soft);
  }
  .contact-list {
    position: absolute;
    top: 348px;
    left: 0;
    margin: 0;
    padding: 0;
    list-style: none;
  }
  .contact-item {
    display: flex;
    align-items: center;
    height: 35px;
    font-size: 23px;
    white-space: nowrap;
  }
  .contact-icon {
    width: 24px;
    height: 24px;
    margin-right: 26px;
    fill: var(--panel-text-soft);
  }
  .postal-address {
    position: absolute;
    top: 462px;
    left: 0;
    margin: 0;
    font-style: normal;
    font-size: 23px;
    line-height: 37px;
    white-space: nowrap;
    color: var(--panel-text-soft);
  }
  .brand-name {
    position: absolute;
    left: 773px;
    top: 410px;
    transform: translateX(-50%);
    margin: 0;
    font-size: 38px;
    font-weight: 600;
    color: var(--brand-text);
    white-space: nowrap;
  }
</style>
</head>
<body>
  <div class="business-card">
    <svg class="card-shapes" width="1000" height="603" viewBox="0 0 1000 603" aria-hidden="true">
      <defs>
        <linearGradient id="panelBlue" x1="0" y1="0" x2="0.3" y2="1">
          <stop offset="0" stop-color="#2a6a95"/>
          <stop offset="1" stop-color="#1b4f78"/>
        </linearGradient>
      </defs>
      <path d="M0,0 H612 Q532,301 612,603 H0 Z" fill="#3a8aa3"/>
      <path d="M0,0 H606 Q520,301 606,603 H0 Z" fill="url(#panelBlue)"/>
    </svg>

    <div class="contact-panel">
      <h1 class="person-name">Dana Reyes Moore</h1>
      <p class="person-role">Managing Director</p>

      <ul class="contact-list">
        <li class="contact-item">
          <svg class="contact-icon" viewBox="0 0 24 24" aria-hidden="true"><path d="M3 7c0-2 4-3 9-3s9 1 9 3v2h-5V7.5c-2-.6-6-.6-8 0V9H3z M6 11h12l2 8H4z M10 14h4v3h-4z"/></svg>
          <span>555.204.3187</span>
        </li>
        <li class="contact-item">
          <svg class="contact-icon" viewBox="0 0 24 24" aria-hidden="true"><path d="M2 5h20v14H2z M4 7v.5l8 6 8-6V7z M4 10v7h16v-7l-8 6z" fill-rule="evenodd"/></svg>
          <span>dana@lodgebridgely.net</span>
        </li>
        <li class="contact-item">
          <svg class="contact-icon" viewBox="0 0 24 24" aria-hidden="true"><path d="M12 2a10 10 0 1 0 0 20 10 10 0 0 0 0-20zm0 2c1.2 1.4 2 3.6 2.2 7H9.8c.2-3.4 1-5.6 2.2-7zM4.1 11a8 8 0 0 1 4.5-6.3A14 14 0 0 0 7.8 11zm0 2h3.7c.1 2.4.4 4.5.8 6.3A8 8 0 0 1 4.1 13zm5.7 0h4.4c-.2 3.4-1 5.6-2.2 7-1.2-1.4-2-3.6-2.2-7zm6.4 0h3.7a8 8 0 0 1-4.5 6.3c.4-1.8.7-3.9.8-6.3zm0-2a14 14 0 0 0-.8-6.3 8 8 0 0 1 4.5 6.3z"/></svg>
          <span>www.lodgebridgely.net</span>
        </li>
      </ul>

      <address class="postal-address">
        318 Marlow Ave., Suite 207.<br>
        Portland, Oregon OR 97205
      </address>
    </div>

    <p class="brand-name">LodgeBridgely</p>
  </div>
</body>
</html>
```